International Consulting Firm
Stationery incl. business cards, letterhead, envelope, PPT template, and brochure
Professional
DMN QRT
CHIEF EXECUTIVE OFFICER
LEVEL 4,
7 MOOR LANE
FERN HOUSE
ASHBURY VALE
DMN@DORSETTPRYCE.EXAMPLE
WWW.DORSETTPRYCE.EXAMPLE
The fonts used in the logo are (a) Eras Bold ITC & (b)BankGothic
Logo only
This fantastic logo was designed recently by quarbin and we now need stationery to support it.

```html
<!DOCTYPE html>
<html lang="en">
<head>
<meta charset="utf-8">
<title>Dorsett Pryce Stationery</title>
<link href="https://fonts.googleapis.com/css2?family=Open+Sans:wght@400;600;700;800&display=swap" rel="stylesheet">
<style>
  :root{
    --ink:#0d0d0d;
    --paper:#ffffff;
    --backdrop:#e4e4e4;
    --muted:#555555;
    --font:"Open Sans", Arial, sans-serif;
  }
  *{box-sizing:border-box;margin:0;padding:0}
  html,body{width:1200px;height:897px;overflow:hidden}
  body{background:var(--backdrop);font-family:var(--font);color:var(--ink);position:relative}
  .piece{position:absolute;overflow:hidden;box-shadow:0 3px 10px rgba(0,0,0,.25)}
  .piece svg.shape{position:absolute;inset:0;width:100%;height:100%}
  .brand{position:absolute;display:flex;align-items:center;gap:6px;font-weight:800;letter-spacing:.04em;white-space:nowrap}
  .brand .dot{border-radius:50%;flex:none}
  .brand-light{color:var(--paper)}
  .brand-light .dot{background:var(--paper)}
  .brand-dark{color:var(--ink)}
  .brand-dark .dot{background:var(--ink)}
  .tagline{position:absolute;font-size:7px;font-weight:600;letter-spacing:.05em;white-space:nowrap}

  /* business card front */
  .card-front{left:100px;top:96px;width:358px;height:211px;background:var(--paper);border-radius:10px}
  .card-front .brand{left:22px;top:150px;font-size:13px}
  .card-front .brand .dot{width:12px;height:12px}
  .card-front .tagline{left:22px;top:172px;color:var(--paper)}
  .card-front .person{position:absolute;right:22px;top:18px;text-align:right}
  .person .name{font-size:16px;font-weight:800}
  .person .role{font-size:9px;font-weight:700;letter-spacing:.03em}
  .card-front .details{position:absolute;right:22px;top:84px;text-align:right;font-size:8px;font-weight:600;line-height:1.45;white-space:nowrap}

  /* business card back */
  .card-back{left:100px;top:336px;width:358px;height:168px;background:var(--ink);border-radius:10px}
  .card-back .brand{left:50%;top:58px;transform:translateX(-50%);font-size:16px}
  .card-back .brand .dot{width:14px;height:14px}
  .card-back .web{position:absolute;left:22px;bottom:20px;font-size:10px;font-weight:700;color:var(--paper)}

  /* letterhead */
  .letterhead{left:487px;top:108px;width:233px;height:400px;background:var(--paper)}
  .letterhead .brand{left:16px;top:24px;font-size:8.5px}
  .letterhead .brand .dot{width:8px;height:8px}
  .letterhead .tagline{left:16px;top:38px;font-size:4.5px}
  .letterhead .contact{position:absolute;left:150px;top:18px;font-size:4.5px;line-height:1.4;font-weight:600;white-space:nowrap}
  .letterhead .body{position:absolute;left:16px;top:66px;width:200px;font-size:4.6px;line-height:1.55;color:var(--muted)}
  .letterhead .body p{margin-bottom:5px}
  .letterhead .web{position:absolute;right:14px;bottom:12px;font-size:6px;font-weight:700;color:var(--paper)}

  /* tall pieces */
  .tall-narrow{left:828px;top:108px;width:84px;height:384px;background:var(--ink)}
  .tall-wide{left:919px;top:108px;width:185px;height:384px;background:var(--paper)}
  .tall-narrow .brand{left:10px;bottom:30px;font-size:6.5px}
  .tall-narrow .brand .dot{width:6px;height:6px}
  .tall-wide .brand{left:14px;bottom:34px;font-size:10px}
  .tall-wide .brand .dot{width:9px;height:9px}
  .tall-wide .web{position:absolute;left:14px;bottom:16px;font-size:7px;font-weight:700}

  /* presentation slides */
  .slide{top:595px;height:209px;background:var(--ink)}
  .slide-title{left:100px;width:283px}
  .slide-content{left:413px;width:307px}
  .slide .heading{position:absolute;color:var(--paper);font-weight:800;font-size:15px;line-height:1.2;white-space:nowrap}
  .slide-title .heading{left:152px;top:20px}
  .slide-content .heading{left:166px;top:20px}
  .slide .brand{font-size:11px}
  .slide .brand .dot{width:10px;height:10px}
  .slide-title .brand{left:14px;top:150px}
  .slide-title .tagline{left:14px;top:168px;font-size:6px}
  .slide-content .brand{right:16px;bottom:28px}
  .slide-content .tagline{right:16px;bottom:16px;font-size:6px;color:var(--paper)}
</style>
</head>
<body>

<section class="piece card-front" aria-label="Business card front">
  <svg class="shape" viewBox="0 0 358 211" preserveAspectRatio="none"><path d="M0 0H150C190 60 190 150 150 211H0Z" fill="#0d0d0d"/></svg>
  <div class="brand brand-light"><span class="dot"></span>DORSETT PRYCE</div>
  <div class="tagline">Advising business worldwide</div>
  <div class="person">
    <div class="name">DMN QRT</div>
    <div class="role">CHIEF EXECUTIVE OFFICER</div>
  </div>
  <div class="details">
    LEVEL 4,<br>7 MOOR LANE, FERN HOUSE<br>ASHBURY VALE<br>P: 0203 555 0148<br>F: 0203 555 0149<br>M: 0770 555 0192<br>DMN@DORSETTPRYCE.EXAMPLE
  </div>
</section>

<section class="piece card-back" aria-label="Business card back">
  <div class="brand brand-light"><span class="dot"></span>DORSETT PRYCE</div>
  <div class="web">WWW.DORSETTPRYCE.EXAMPLE</div>
</section>

<section class="piece letterhead" aria-label="Letterhead">
  <svg class="shape" viewBox="0 0 233 400" preserveAspectRatio="none"><path d="M233 330C170 330 120 360 90 400H233Z" fill="#0d0d0d"/></svg>
  <div class="brand brand-dark"><span class="dot"></span>DORSETT PRYCE</div>
  <div class="tagline">Advising business worldwide</div>
  <div class="contact">LEVEL 4,<br>7 MOOR LANE<br>FERN HOUSE<br>ASHBURY VALE<br>P: 0203 555 0148</div>
  <div class="body">
    <p>12 March 2024<br>Mr Sample Client<br>Ashbury Vale</p>
    <p>Dear Client,</p>
    <p>Thank you for meeting with our team last week. We have prepared a short outline of the consulting services we discussed, together with a timeline and budget for your review.</p>
    <p>Please let us know if any part needs further detail. We look forward to working with you.</p>
    <p>Yours sincerely,<br>DMN QRT</p>
  </div>
  <div class="web">WWW.DORSETTPRYCE.EXAMPLE</div>
</section>

<section class="piece tall-narrow" aria-label="Compliment slip">
  <svg class="shape" viewBox="0 0 84 384" preserveAspectRatio="none"><path d="M84 40C30 90 30 250 84 300Z" fill="#ffffff"/></svg>
  <div class="brand brand-light"><span class="dot"></span>DORSETT PRYCE</div>
</section>

<section class="piece tall-wide" aria-label="Brochure cover">
  <svg class="shape" viewBox="0 0 185 384" preserveAspectRatio="none"><path d="M0 0H185V300C120 240 40 260 0 300Z" fill="#0d0d0d"/></svg>
  <div class="brand brand-dark"><span class="dot"></span>DORSETT PRYCE</div>
  <div class="web">WWW.DORSETTPRYCE.EXAMPLE</div>
</section>

<section class="piece slide slide-title" aria-label="Presentation title slide">
  <svg class="shape" viewBox="0 0 283 209" preserveAspectRatio="none"><path d="M0 0H110C150 60 150 150 110 209H0Z" fill="#ffffff"/></svg>
  <h1 class="heading">Welcome to our<br>Presentation</h1>
  <div class="brand brand-dark"><span class="dot"></span>DORSETT PRYCE</div>
  <div class="tagline">Advising business worldwide</div>
</section>

<section class="piece slide slide-content" aria-label="Presentation content slide">
  <svg class="shape" viewBox="0 0 307 209" preserveAspectRatio="none"><path d="M0 0H120C160 70 150 150 100 209H0Z" fill="#ffffff"/></svg>
  <h2 class="heading">Welcome to our<br>Presentation</h2>
  <div class="brand brand-light"><span class="dot"></span>DORSETT PRYCE</div>
  <div class="tagline">Advising business worldwide</div>
</section>

</body>
</html>
```